Copyright Registration Service Website

Brightvaultly.com (site can be accessed) is a website that will enable artists, photographers, writers, sculptors, musicians and other creative persons of all media to register their works of authorship with the U.S. Ashgrove National Repository, Merriton Bureau, for a nominal fee of $99 plus filing fees (in most cases). The high points of marketing are (1) every application is reviewed by a lawyer and (2) the entire copyright process is monitored, as part of the service fee. There are 8 categories of copyrightability:
Literary Works
Dramatic Works
Musical Works
Sound Recordings
Motion Pictures
Choreographic and Pantomime Works
Photographs, Paintings and Sculptures
Architectural Works
Please look at the existing site; provide a better landing page than currently exists. In particular, the logo is in need of serious improvement. We would like it to be bright and sunny; visually pleasant and witty; and clever but not "doctoral" in presentation. Thank you for your participation.

Target Market(s)

photographers, artists, musicians, age groups of 20-50

Industry/Entity Type

Marketing

Requirements
Should not have
• stiffness

```html
<!DOCTYPE html>
<html lang="en">
<head>
<meta charset="utf-8">
<title>Brightvaultly — Copyright Registration</title>
<link href="https://fonts.googleapis.com/css2?family=Open+Sans:wght@400;600;700&family=Roboto+Condensed:wght@300;400;700&display=swap" rel="stylesheet">
<style>
:root{
  --blue:#1e88d6;
  --blue-dark:#0f5fa3;
  --nav:#1b7cc8;
  --yellow:#f5c400;
  --red:#d9262c;
  --ink:#333c44;
  --muted:#7a8590;
  --page:#ececec;
  --panel:#ffffff;
  --rule:#d9dde1;
  --footer:#1f2225;
  --footer-deep:#141618;
  --footer-text:#9aa3ab;
}
*{box-sizing:border-box;margin:0;padding:0}
html,body{width:745px;height:1200px;overflow:hidden}
body{background:var(--page);font-family:"Open Sans",sans-serif;color:var(--ink);position:relative;font-size:7px;line-height:1.45}
.top-bar{position:absolute;left:0;top:0;width:745px;height:44px;background:#fff;display:flex;align-items:center;justify-content:space-between;padding:0 62px}
.brand{display:flex;align-items:center;gap:6px;font-family:"Roboto Condensed",sans-serif;font-weight:700;font-size:17px;color:var(--blue-dark);letter-spacing:.5px}
.brand-mark{width:14px;height:14px;border-radius:50%;background:var(--yellow)}
.call{display:flex;align-items:center;gap:5px;font-size:7px;color:var(--muted);font-weight:600}
.call strong{color:var(--blue-dark);font-size:10px}
.call .social{display:flex;gap:3px;margin-left:6px}
.call .social span{width:9px;height:9px;background:var(--blue);border-radius:2px}
.main-nav{position:absolute;left:62px;top:44px;width:620px;height:18px;background:var(--nav);display:flex}
.main-nav a{color:#fff;text-decoration:none;font-weight:700;font-size:6.5px;letter-spacing:.3px;padding:0 10px;line-height:18px;border-right:1px solid rgba(255,255,255,.2)}
.main-nav a.current{background:var(--yellow);color:var(--blue-dark)}
.hero{position:absolute;left:0;top:62px;width:745px;height:312px;background:linear-gradient(180deg,#e6e9ec 0%,#cfd5da 70%,#b9c0c6 100%)}
.hero-copy{position:absolute;left:36px;top:40px;width:245px;background:rgba(255,255,255,.78);padding:12px 14px}
.hero-copy .kicker{font-family:"Roboto Condensed",sans-serif;font-size:16px;color:var(--ink);line-height:1.15}
.hero-copy .big{font-family:"Roboto Condensed",sans-serif;font-weight:700;font-size:42px;color:var(--blue);line-height:1}
.hero-copy .price{font-family:"Roboto Condensed",sans-serif;font-size:13px;color:var(--ink)}
.hero-copy .note{font-size:7px;color:var(--muted);font-weight:600}
.btn{display:inline-block;background:var(--red);color:#fff;font-weight:700;font-size:6.5px;padding:5px 10px;margin-top:9px}
.btn-small{background:var(--blue-dark);padding:3px 7px;font-size:5.5px;margin-top:6px}
.video{position:absolute;left:315px;top:80px;width:215px;height:150px;background:linear-gradient(135deg,#f3f1ec,#c8c2b4);border:4px solid #fff;box-shadow:0 2px 6px rgba(0,0,0,.25)}
.video svg{position:absolute;left:87px;top:55px}
.presenter{position:absolute;left:520px;top:24px;width:195px;height:288px;background:linear-gradient(180deg,#c9c4bd,#6f6a66)}
.slider-dots{position:absolute;left:36px;top:236px;display:flex;gap:3px}
.slider-dots span{width:9px;height:9px;background:#fff;color:var(--ink);font-size:5px;text-align:center;line-height:9px}
.slider-dots span.on{background:var(--blue);color:#fff}
.content{position:absolute;left:62px;top:386px;width:620px;height:588px;background:var(--panel);padding:22px 14px}
.sidebar{position:absolute;left:14px;top:22px;width:122px}
.side-box{border:1px solid var(--rule);padding:9px 10px}
.side-box h3{font-family:"Roboto Condensed",sans-serif;font-size:12px;color:var(--blue);font-weight:400;line-height:1.1}
.side-box h3 b{display:block;color:var(--ink);font-size:14px;font-weight:700}
.cat-list{list-style:none;margin-top:7px}
.cat-list li{border-bottom:1px solid var(--rule);font-size:6px;padding:2.5px 0 2.5px 8px;position:relative}
.cat-list li::before{content:"›";position:absolute;left:1px;color:var(--blue)}
.testimonial{margin-top:12px;background:var(--blue);color:#fff;padding:9px 10px 12px}
.testimonial h3{font-family:"Roboto Condensed",sans-serif;font-size:12px;font-weight:400;color:var(--yellow);line-height:1.1}
.testimonial h3 b{display:block;color:#fff;font-size:14px}
.testimonial p{font-size:6px;margin-top:6px;font-style:italic}
.client{display:flex;align-items:center;gap:6px;margin-top:8px;font-size:6px}
.client .avatar{width:24px;height:24px;border-radius:50%;background:#d9cfc4}
.client b{display:block;font-size:6.5px}
.main{position:absolute;left:166px;top:22px;width:440px}
.welcome{font-family:"Roboto Condensed",sans-serif;font-weight:300;color:var(--muted);font-size:26px;line-height:1.05}
.welcome b{display:block;color:var(--blue);font-weight:400;font-size:30px}
.lead{font-size:7.5px;color:var(--muted);margin-top:6px;text-transform:uppercase;font-weight:600}
.main p.body{font-size:6.5px;margin-top:8px;color:#555}
.callout{margin-top:14px;background:#eef0f2;padding:14px 20px;text-align:center;font-size:8px;color:var(--muted);text-transform:uppercase;border:1px solid var(--rule)}
.callout em{font-style:normal;color:var(--blue)}
.section-title{font-family:"Roboto Condensed",sans-serif;font-size:17px;font-weight:300;color:var(--ink);margin-top:16px;border-bottom:1px solid var(--rule);padding-bottom:3px}
.section-title b{color:var(--blue);font-weight:400}
.statute{display:flex;gap:14px;margin-top:12px}
.statute .thumb{width:120px;height:80px;flex:none;background:linear-gradient(135deg,#eceae4,#b8b2a6);border:3px solid #fff;box-shadow:0 1px 4px rgba(0,0,0,.3)}
.statute h4{font-family:"Roboto Condensed",sans-serif;font-size:14px;font-weight:400;color:var(--ink)}
.statute h5{font-size:6.5px;color:var(--muted);font-weight:600}
.statute p{font-size:6.5px;color:#555;margin-top:5px}
.footer{position:absolute;left:0;top:986px;width:745px;height:214px;background:var(--footer);color:var(--footer-text)}
.footer-cols{display:flex;padding:16px 62px 0;gap:20px}
.footer-cols div{flex:1}
.footer-cols h4{font-family:"Roboto Condensed",sans-serif;color:#fff;font-size:11px;font-weight:400;border-bottom:1px solid #3a3f44;padding-bottom:4px;margin-bottom:5px}
.footer-cols ul{list-style:none}
.footer-cols li{font-size:6px;padding:1.5px 0}
.footer-cols p{font-size:6px}
.footer-cols p b{color:#fff}
.contact li{display:flex;align-items:center;gap:5px}
.disclaimer{margin:14px 62px 0;font-size:5.5px;border-top:1px solid #3a3f44;padding-top:8px}
.disclaimer b{color:#fff}
.copyright{position:absolute;left:0;bottom:0;width:745px;height:24px;background:var(--footer-deep);text-align:center;line-height:24px;font-size:6px}
</style>
</head>
<body>
<header class="top-bar">
  <div class="brand"><span class="brand-mark"></span>BRIGHTVAULTLY</div>
  <div class="call">
    <svg width="9" height="9" viewBox="0 0 10 10"><path d="M2 1l2 2-1 1.5c.6 1.2 1.3 1.9 2.5 2.5L7 6l2 2-1.5 1.5C4.5 9 1 5.5.5 2.5z" fill="#0f5fa3"/></svg>
    CALL US <strong>1 800 555 0142</strong>
    <div class="social"><span></span><span></span><span></span><span></span></div>
  </div>
</header>
<nav class="main-nav">
  <a class="current">HOME</a><a>ABOUT US</a><a>COPYRIGHT CATEGORIES</a><a>LAW &amp; STATUTES</a><a>COPYRIGHT PROCESS</a><a>CONTACT US</a><a>LINKS</a>
</nav>
<section class="hero">
  <div class="hero-copy" style="top:0;left:0;width:745px;height:312px;background:none;padding:0" role="img" aria-label="Bright modern office interior photograph"></div>
  <div class="hero-copy">
    <div class="kicker">PROTECT YOUR<br>COPYRIGHT IN 5 MINUTES!</div>
    <div class="big">COPYRIGHT</div>
    <div class="price">REGISTRATION <b>$99</b> (MOST CASES)</div>
    <div class="note">ENTIRE PROCESS IS REVIEWED BY A LAWYER</div>
    <span class="btn">LEARN MORE ▸</span>
  </div>
  <div class="video" role="img" aria-label="Introduction video still of a sunny studio desk">
    <svg width="40" height="30" viewBox="0 0 40 30"><rect width="40" height="30" rx="6" fill="#d9262c"/><path d="M16 9l10 6-10 6z" fill="#fff"/></svg>
  </div>
  <div class="presenter" role="img" aria-label="Friendly lawyer giving a thumbs up"></div>
  <div class="slider-dots"><span class="on">1</span><span>2</span><span>3</span></div>
</section>
<main class="content">
  <aside class="sidebar">
    <div class="side-box">
      <h3>COPYRIGHT<b>CATEGORIES</b></h3>
      <ul class="cat-list">
        <li>Literary</li><li>Dramatic</li><li>Musical</li><li>Sound Recordings</li><li>Motion Pictures</li><li>Choreographic</li><li>Pantomimes</li><li>Sculptures</li><li>Photographs</li><li>Paintings</li><li>Sculptures</li><li>Architectural</li>
      </ul>
    </div>
    <div class="testimonial">
      <h3>OUR CLIENT<b>TESTIMONIALS</b></h3>
      <p>"Registering my photo series took minutes and a real lawyer checked every detail. I finally feel my work is safe and truly mine."</p>
      <div class="client"><span class="avatar" role="img" aria-label="Client portrait"></span><div><b>MARLA PENROSE</b>Portland, OR</div></div>
    </div>
  </aside>
  <section class="main">
    <h1 class="welcome">WELCOME TO<b>BRIGHTVAULTLY</b></h1>
    <div class="lead">Every application is individually filed and monitored under lawyer supervision. Protect your intellectual property rights</div>
    <p class="body">Are you an artist or otherwise engaged in a creative field? In the modern age, it is vital to protect your artistic, intellectual and moral rights that exist in your works of authorship. The current copyright act provides protection for each work of authorship that is fixed in a tangible medium of expression. Once a copyright registration is created, it protects your creative authorship forever, with your artistic expression being preserved in the Ashgrove National Repository through the Merriton Bureau.</p>
    <p class="body">Every application is reviewed by a licensed lawyer knowledgeable with the copyright registration process. At a large law firm, registration fees can cost thousands of dollars. Even small firms charge hundreds or even more for the same service because intellectual property lawyers bill by the hour, often well above a fair rate for artists.</p>
    <div class="callout">Every application is individually filed and monitored under lawyer supervision. <em>Protect your intellectual property rights</em></div>
    <h2 class="section-title"><b>LAW &amp;</b> STATUTES</h2>
    <div class="statute">
      <div class="thumb" role="img" aria-label="Law books and gavel on a desk"></div>
      <div>
        <h4>REGISTRATION $99 (MOST CASES)</h4>
        <h5>ENTIRE PROCESS IS REVIEWED BY A LAWYER</h5>
        <p>Our simple service guides you through each step, files the form for you and watches the status until your certificate arrives. No hidden costs, no confusing legal terms, only clear help from a real attorney who cares about creative work.</p>
        <span class="btn btn-small">LEARN MORE ▸</span>
      </div>
    </div>
  </section>
</main>
<footer class="footer">
  <div class="footer-cols">
    <div><h4>SITE MAP</h4><ul><li>› Home</li><li>› About Us</li><li>› Copyright Categories</li><li>› Law &amp; Statutes</li><li>› Copyright Process</li><li>› Contact Us</li><li>› Links</li></ul></div>
    <div><h4>QUICK LINKS</h4><ul><li>› Why register now</li><li>› Fees and pricing</li><li>› How the process works</li><li>› Meet our lawyers</li><li>› Client stories</li><li>› Privacy policy</li></ul></div>
    <div><h4>FAQ'S</h4><p><b>Shipping &amp; Delivery</b><br>How long does a filing take? Most forms are sent the same day.</p><p style="margin-top:5px"><b>Payment methods</b><br>We accept all major cards and bank transfer.</p></div>
    <div class="contact"><h4>CONTACT US</h4><ul>
      <li><svg width="7" height="9" viewBox="0 0 8 10"><path d="M4 0a4 4 0 014 4c0 3-4 6-4 6S0 7 0 4a4 4 0 014-4z" fill="#1e88d6"/></svg>48 Larkfield Way, Suite 3</li>
      <li><svg width="7" height="7" viewBox="0 0 10 10"><path d="M2 1l2 2-1 1.5c.6 1.2 1.3 1.9 2.5 2.5L7 6l2 2-1.5 1.5C4.5 9 1 5.5.5 2.5z" fill="#1e88d6"/></svg>1 800 555 0142</li>
      <li><svg width="8" height="6" viewBox="0 0 10 7"><rect width="10" height="7" fill="#1e88d6"/><path d="M0 0l5 4 5-4" stroke="#1f2225" fill="none"/></svg>hello@brightvaultly.com</li>
    </ul></div>
  </div>
  <p class="disclaimer"><b>DISCLAIMER:</b> Information on this site is general in nature and is not legal advice. Use of this site does not create a lawyer and client relationship. Fees shown cover our service only; government filing fees are extra in most cases. Results depend on each work and may vary.</p>
  <div class="copyright">© 2014 Brightvaultly.com | All Rights Reserved</div>
</footer>
</body>
</html>
```